Professional Website Design to match new logo for Medical Legal Company

We have rebranded our company and We want a professional but also dynamic web site design for a group of esteemed doctors that provide expert evaluation of an injured worker in a Workers Compensation case.
​
1. Our target market is both the attorneys who select our doctors and any doctors who would wish to join our group.

2. Notes for the Landing Page:
- We prefer a simpler, sleeker more modern look for the landing page.
- We want a simplified landing page with one image, three buttons highlighted in Content document.
- We want the main image to be black and white but it can be splashed with color.
-We think the landing page might be enhanced by add a dark blue or black as a primary color. Of course please feel free to try any color combination you think might work.
- We want "The Meridale Circle" in large letters and "Stewards of a fair and prompt outcome" in small lettering. We don't want icons on the buttons.
- Do not want more than the one picture at top of landing page.
- We do not want any pictures that include faces. Please eliminate or replace. They will not be chosen.
- For the landing page, instead of a second set of photos please experiment with using medical symbols and legal symbols.
​
3. New Company Name: The Meridale Circle
New logo is uploaded bronze and grey/silver will be colors although we are still tweaking the colors for more metallic feel. Want simple not busy.

4. The overall Web page design needs to have some website design effect (e,g image rollover, scrolling effect, hover effect etc).

5. Please follow the attached word document file for the page content of the 4 web pages. Do not mix it up.

Previous company website: www.clinicjuristpanel.example (we wish to convert some of the content from this website to the new brand). Competitor website that we like: www.docboardly.example

Target Market(s)

Professional Elite. Attorneys and Doctors

Industry/Entity Type

Medical Legal

Coding

Coded - Design and coding required

Number of Pages Required

5+ page

Font styles to use
Other font styles liked:
• Helvetica or maybe font that matches logo. We are open

Colors

Designer to choose colors to be used in the design.

Requirements
Must have
• I can't locate on color scale but we want Bronze and Silver/Grey from logo. Additional colors can be added. Various shades of grey
Nice to have
• Black and white photos, simple elegant design
Should not have
• Images with faces of unknown people

```html
<!DOCTYPE html>
<html lang="en">
<head>
<meta charset="utf-8">
<title>The Meridale Circle</title>
<link rel="stylesheet" href="https://fonts.googleapis.com/css2?family=Crimson+Pro:wght@400;600&family=Jost:wght@400;500&display=swap">
<style>
:root{
  --bg:#f0f0f0;
  --bg-light:#f9f9f9;
  --ink:#3c3c3c;
  --ink-soft:#4a4a4a;
  --rule:#d6d6d6;
  --bronze-a:#c98a5a;
  --bronze-b:#9a5f34;
  --btn-grey:#e2e2e2;
  --btn-text:#7a7a7a;
  --band:#3f3f3f;
  --white:#ffffff;
}
*{margin:0;padding:0;box-sizing:border-box}
html,body{width:888px;height:1200px;overflow:hidden}
body{background:var(--bg);color:var(--ink);font-family:"Jost",sans-serif;position:relative}
a{color:inherit;text-decoration:none}

.site-header{position:absolute;left:25px;top:0;width:838px;height:53px;border-bottom:1px solid var(--rule)}
.brand{position:absolute;left:0;top:14px;display:flex;align-items:center;gap:6px}
.brand-mark{width:12px;height:12px;background:var(--bronze-b)}
.brand-name{font-family:"Crimson Pro",serif;font-weight:600;font-size:16px;color:#6b6b6b}
.main-nav{position:absolute;right:0;top:21px;display:flex;gap:27px;font-size:9.6px;font-weight:500;color:var(--ink-soft)}

.intro-head{position:absolute;left:25px;top:80px}
.intro-head h1{font-family:"Crimson Pro",serif;font-weight:400;font-size:33px;line-height:1;color:var(--ink)}
.intro-head p{font-size:9.4px;margin-top:6px;color:var(--ink-soft)}
.cta-row{position:absolute;left:499px;top:88px;display:flex;gap:5px}
.cta{width:118px;height:32px;display:flex;align-items:center;justify-content:center;font-size:10px;font-weight:500;background:var(--btn-grey);color:var(--btn-text)}
.cta--primary{background:linear-gradient(90deg,var(--bronze-a),var(--bronze-b));color:var(--white)}

.lower-bg{position:absolute;left:0;top:391px;width:888px;height:253px;background:var(--bg-light)}
.hero{position:absolute;left:25px;top:148px;width:838px;height:305px;background:linear-gradient(135deg,#d9d9d9 0%,#b8b8b8 35%,#9a7048 50%,#cfcfcf 62%,#e6e6e6 100%)}

.lead{position:absolute;left:25px;top:503px;width:420px;font-family:"Crimson Pro",serif;font-size:22.5px;line-height:31px;color:var(--ink)}
.lead-aside{position:absolute;left:516px;top:529px;width:340px;font-size:10.6px;line-height:20px;color:var(--ink-soft)}

.updates-title{position:absolute;left:25px;top:668px;font-family:"Crimson Pro",serif;font-size:16px;font-weight:600;color:var(--ink)}
.update{position:absolute;width:262px;border-bottom:1px solid var(--rule);padding-bottom:12px}
.update time{display:block;font-size:9.4px;color:var(--ink-soft);margin-bottom:9px}
.update h3{font-family:"Crimson Pro",serif;font-weight:600;font-size:12.6px;line-height:20px;color:var(--ink)}

.newsletter{position:absolute;left:0;top:826px;width:888px;height:52px;background:var(--band);color:var(--white);font-size:9.6px;font-weight:500}
.newsletter span{position:absolute;left:26px;top:19px}
.newsletter a{position:absolute;right:27px;top:19px;text-decoration:underline;text-underline-offset:2px}

.footer-brand{position:absolute;left:25px;top:920px;display:flex;align-items:center;gap:8px}
.footer-brand .brand-mark{width:18px;height:18px}
.footer-brand .brand-name{font-size:24px}
.hq{position:absolute;left:25px;top:984px;font-size:9.4px;line-height:17.3px;color:var(--ink-soft);font-style:normal}
.hq strong{font-weight:500;color:var(--ink)}
.contact-lines{margin-top:14px}
.copyright{position:absolute;left:25px;top:1161px;font-size:9.4px;color:var(--ink-soft)}
.foot-col{position:absolute;top:917px;font-size:9.4px;color:var(--ink-soft)}
.foot-col h4{font-weight:500;font-size:9.6px;color:var(--ink);margin-bottom:7px}
.foot-col li{list-style:none;height:19.7px}
.foot-col ul + h4{margin-top:9px}
</style>
</head>
<body>
<header class="site-header">
  <a class="brand" href="#"><span class="brand-mark"></span><span class="brand-name">The Meridale Circle</span></a>
  <nav class="main-nav"><a href="#">Services</a><a href="#">Stakeholders</a><a href="#">Physicians</a><a href="#">Meridale Gives Back</a></nav>
</header>

<div class="lower-bg"></div>

<section class="intro-head">
  <h1>The Meridale Circle</h1>
  <p>Stewards of a fair and prompt outcome</p>
</section>
<div class="cta-row">
  <a class="cta cta--primary" href="#">Stakeholders</a>
  <a class="cta" href="#">Physicians</a>
  <a class="cta" href="#">Member Login</a>
</div>

<div class="hero" role="img" aria-label="Black and white photo of a bronze-tubed stethoscope resting on a clipboard beside a laptop keyboard"></div>

<p class="lead">The Meridale Circle is a leader in Qualified Medical Evaluations and SIBTF cases in the State of California.</p>
<p class="lead-aside">Our doctors are dedicated to facilitating settlements through rapid, objective and well researched Expert Medical Opinions.</p>

<h2 class="updates-title">Our Recent Updates:</h2>
<article class="update" style="left:25px;top:716px"><time>16 March 2024</time><h3>More Changes To QME Appointments On The Horizon.</h3></article>
<article class="update" style="left:313px;top:713px"><time>16 March 2024</time><h3>Qualified Medical Evaluator (QME) Regulations – Telehealth Extended Until July 17, 2022.</h3></article>
<article class="update" style="left:602px;top:713px"><time>16 March 2024</time><h3>Health Agency Awards Grants To Address Health Care Worker Burnout, Improve Mental Health, Well-Being.</h3></article>

<div class="newsletter"><span>Most Recent Newsletter</span><a href="#">Download now</a></div>

<div class="footer-brand"><span class="brand-mark"></span><span class="brand-name">The Meridale Circle</span></div>
<address class="hq">
  <strong>Headquarters</strong><br>2280 Larkspur Ave.<br>3rd Floor<br>Fernhollow, CA 90412
  <div class="contact-lines"><strong>Call toll free</strong> (800) 555-0142<br><strong>Fax</strong> (310) 555-0187</div>
</address>
<p class="copyright">© 2022 Clinic Jurist Panel</p>

<div class="foot-col" style="left:366px">
  <h4>About</h4><ul><li>Company</li><li>QME Locations</li><li>Privacy Policy</li><li>Careers</li></ul>
  <h4>Join Us</h4><ul><li>Join our network</li></ul>
  <h4>Blog</h4><ul><li>Blog</li></ul>
</div>
<div class="foot-col" style="left:494px">
  <h4>Education</h4><ul><li>Live Seminar QME Report Writing Course</li><li>Online QME Report Writing Course</li><li>QME Continuing Education (CEU)</li><li>Impairment Guides 6th Edition IME Training</li></ul>
  <h4>Contact</h4><ul><li>Exam Request</li><li>FAQ</li><li>Locations</li><li>Contact Info</li></ul>
  <h4>Login</h4><ul><li>Login To Your Account</li></ul>
</div>
<div class="foot-col" style="left:728px">
  <h4>Services</h4><ul><li>IME</li><li>AME</li><li>QME</li><li>Subsequent Injuries Fund</li><li>Ergonomic Evaluations</li><li>Measuring Workers</li><li>Pre-Employment Screenings</li><li>Fit for Duty</li><li>Functional Capacity Evaluation</li><li>FCE &amp; Care Guidelines</li><li>Physician’s Guide</li><li>Impairment Rating</li></ul>
</div>
</body>
</html>
```